Plumbing Company business card design

Create a business card for our plumbing company. Following info needs to be present

Website-prairiepipeworks.com
Email- contact@prairiepipeworks-mail.com
Phone-515-394-2068
Address-4817 NW Cobalt Blvd STE K
Ankeny, Iowa 50347

```html
<!DOCTYPE html>
<html lang="en">
<head>
<meta charset="utf-8">
<title>Prairie Pipeworks – Business Card</title>
<link href="https://fonts.googleapis.com/css2?family=Montserrat:wght@400;500;700&display=swap" rel="stylesheet">
<style>
  :root {
    --brand-red: #ee2a2a;
    --brand-red-deep: #d92424;
    --brand-blue: #1d4fa0;
    --ink: #1a1a1a;
    --paper: #ffffff;
    --backdrop: #d9d9d9;
  }
  * { box-sizing: border-box; margin: 0; padding: 0; }
  html, body {
    width: 1200px; height: 856px; overflow: hidden;
    background: var(--backdrop);
    font-family: "Montserrat", sans-serif;
  }
  .sheet {
    width: 1200px; height: 856px;
    display: flex; flex-direction: column; align-items: center; justify-content: center;
    gap: 40px;
  }
  .card {
    width: 640px; height: 366px;
    position: relative; overflow: hidden;
    box-shadow: 0 8px 22px rgba(0,0,0,.25);
  }
  /* Front */
  .card-front { background: var(--paper); }
  .brand {
    position: absolute; top: 62px; left: 0; right: 0;
    display: flex; align-items: center; justify-content: center; gap: 16px;
  }
  .brand-dot {
    width: 54px; height: 54px; border-radius: 50%;
    background: var(--brand-red);
  }
  .brand-name {
    font-weight: 700; font-size: 34px; letter-spacing: 1px;
    color: var(--brand-red); text-transform: uppercase;
  }
  .brand-rule {
    position: absolute; top: 140px; left: 150px; right: 150px;
    height: 2px; background: var(--brand-blue);
  }
  .contacts {
    position: absolute; top: 176px; left: 0; right: 0;
    display: flex; flex-direction: column; align-items: center; gap: 12px;
    color: var(--ink); font-size: 15px; font-weight: 500;
  }
  .contact-row { display: flex; align-items: center; gap: 18px; }
  .contact-item { display: flex; align-items: center; gap: 8px; }
  .contact-item svg { width: 18px; height: 18px; flex: none; }
  .address-row {
    display: flex; align-items: center; gap: 14px; margin-top: 6px;
  }
  .address-rule { width: 80px; height: 2px; background: var(--brand-red); }
  /* Back */
  .card-back { background: var(--brand-red); }
  .back-pattern {
    position: absolute; inset: 0;
    background: linear-gradient(135deg, var(--brand-red) 0%, var(--brand-red-deep) 100%);
  }
  .back-brand {
    position: absolute; right: 44px; top: 50%; transform: translateY(-50%);
    display: flex; align-items: center; gap: 10px;
  }
  .back-dot { width: 30px; height: 30px; border-radius: 50%; background: var(--paper); }
  .back-name {
    font-weight: 700; font-size: 16px; letter-spacing: 1px;
    color: var(--paper); text-transform: uppercase;
  }
</style>
</head>
<body>
<main class="sheet">
  <section class="card card-front">
    <div class="brand">
      <span class="brand-dot"></span>
      <span class="brand-name">Prairie Pipeworks</span>
    </div>
    <div class="brand-rule"></div>
    <div class="contacts">
      <div class="contact-item">
        <svg viewBox="0 0 20 20"><circle cx="10" cy="10" r="10" fill="#ee2a2a"/><path d="M6.5 5.5l2 0 1 2.5-1.3 1a6 6 0 0 0 2.8 2.8l1-1.3 2.5 1 0 2c0 .6-.5 1-1 1A8 8 0 0 1 5.5 6.5c0-.6.4-1 1-1z" fill="#fff"/></svg>
        <span>515-394-2068</span>
      </div>
      <div class="contact-row">
        <div class="contact-item">
          <svg viewBox="0 0 20 20"><circle cx="10" cy="10" r="10" fill="#ee2a2a"/><rect x="5" y="6.5" width="10" height="7" fill="none" stroke="#fff" stroke-width="1.3"/><path d="M5 6.5l5 4 5-4" fill="none" stroke="#fff" stroke-width="1.3"/></svg>
          <span>contact@prairiepipeworks-mail.com</span>
        </div>
        <div class="contact-item">
          <svg viewBox="0 0 20 20"><circle cx="10" cy="10" r="10" fill="#ee2a2a"/><circle cx="10" cy="10" r="5" fill="none" stroke="#fff" stroke-width="1.3"/><path d="M5 10h10M10 5c-2.5 3-2.5 7 0 10M10 5c2.5 3 2.5 7 0 10" fill="none" stroke="#fff" stroke-width="1.1"/></svg>
          <span>www.prairiepipeworks.com</span>
        </div>
      </div>
      <div class="address-row">
        <span class="address-rule"></span>
        <span>4817 NW Cobalt Blvd STE K Ankeny, Iowa 50347</span>
        <span class="address-rule"></span>
      </div>
    </div>
  </section>

  <section class="card card-back">
    <div class="back-pattern" role="img" aria-label="Repeating tonal pattern of the company mark across the red card back"></div>
    <div class="back-brand">
      <span class="back-dot"></span>
      <span class="back-name">Prairie Pipeworks</span>
    </div>
  </section>
</main>
</body>
</html>
```